Tranquilly Balanced Restoration

We want to design a business card that is modern and appealing for an innovative psychedelic telemedicine company that provides at-home ketamine-assisted therapy along with wellness, longevity, and anti-aging medicines. We want to use our deep purple and white plus other colors you can find on our website. We don't have any strict brand guidelines yet so feel free to get creative. We want a very professional, but technology first modern design that will instill trust, peace, calm, but also be attractive to investors in the healthcare and SaaS space.

```html
<!DOCTYPE html>
<html lang="en">
<head>
<meta charset="utf-8">
<title>Tranquilly Balanced Restoration — Business Card</title>
<link href="https://fonts.googleapis.com/css2?family=Jost:wght@400;500;600&display=swap" rel="stylesheet">
<style>
  :root {
    --backdrop: #2a2a2c;
    --violet-deep: #6f5fae;
    --violet: #7a65b3;
    --orchid: #a0609a;
    --orchid-text: #b0629f;
    --ink: #3a3a3f;
    --paper: #ffffff;
    --paper-shade: #ececf0;
    --rule: #9b8ec4;
  }
  * { margin: 0; padding: 0; box-sizing: border-box; }
  html, body {
    width: 1200px; height: 900px; overflow: hidden;
    background: var(--backdrop);
    font-family: "Jost", sans-serif;
  }
  .stage { position: relative; width: 1200px; height: 900px; }
  .card {
    position: absolute; left: 285px;
    width: 630px; height: 360px;
    border-radius: 34px 34px 34px 34px;
    overflow: hidden;
  }
  /* Front */
  .card-front {
    top: 50px;
    background: linear-gradient(20deg, var(--orchid) 0%, #8b63a6 50%, var(--violet-deep) 100%);
    display: flex; align-items: center; justify-content: center;
  }
  .front-brand {
    display: flex; align-items: center; gap: 18px;
    color: var(--paper);
    font-weight: 400; font-size: 40px; letter-spacing: 0.5px;
    line-height: 1.1;
  }
  .front-brand .brand-dot {
    width: 26px; height: 26px; border-radius: 50%;
    background: var(--paper); flex: none;
  }
  /* Back */
  .card-back {
    top: 490px;
    background: linear-gradient(160deg, var(--paper-shade) 0%, var(--paper) 55%);
  }
  .person { position: absolute; left: 44px; top: 40px; }
  .person-name {
    color: var(--violet);
    font-weight: 600; font-size: 24px; letter-spacing: 0.5px;
    text-transform: uppercase;
  }
  .person-title { color: var(--ink); font-size: 18px; margin-top: 4px; }
  .back-brand {
    position: absolute; left: 44px; bottom: 46px; width: 250px;
    display: flex; align-items: center; gap: 12px;
    color: var(--orchid-text);
    font-weight: 400; font-size: 26px; line-height: 1.15;
  }
  .back-brand .brand-dot {
    width: 18px; height: 18px; border-radius: 50%;
    background: var(--violet); flex: none;
  }
  .divider {
    position: absolute; left: 318px; top: 150px;
    width: 1px; height: 170px; background: var(--rule);
  }
  .contact { position: absolute; left: 342px; top: 156px; list-style: none; }
  .contact li {
    display: flex; align-items: flex-start; gap: 10px;
    color: var(--ink); font-size: 16.5px; line-height: 1.3;
    margin-bottom: 9px;
  }
  .contact svg { width: 16px; height: 16px; flex: none; margin-top: 2px; fill: var(--orchid-text); }
</style>
</head>
<body>
<main class="stage">
  <section class="card card-front" aria-label="Card front">
    <div class="front-brand">
      <span class="brand-dot"></span>
      <span>Tranquilly Balanced<br>Restoration</span>
    </div>
  </section>

  <section class="card card-back" aria-label="Card back">
    <div class="person">
      <p class="person-name">Maren Ellison, FNP-C</p>
      <p class="person-title">Co-founder, Chief Clinical Officer</p>
    </div>

    <div class="back-brand">
      <span class="brand-dot"></span>
      <span>Tranquilly Balanced Restoration</span>
    </div>

    <div class="divider"></div>

    <ul class="contact">
      <li>
        <svg viewBox="0 0 16 16"><path d="M3.5 1.5l2.5 0 1 3.5-1.7 1.2a8 8 0 0 0 4.5 4.5L11 9l3.5 1v2.5c0 1-1 2-2 2C6.5 14.5 1.5 9.5 1.5 3.5c0-1 1-2 2-2z"/></svg>
        800-555-0142
      </li>
      <li>
        <svg viewBox="0 0 16 16"><path d="M1 3h14v10H1z M1.8 3.8L8 8.5l6.2-4.7" fill="none" stroke="#b0629f" stroke-width="1.6"/></svg>
        hello@tranquillybalanced.com
      </li>
      <li>
        <svg viewBox="0 0 16 16"><circle cx="8" cy="8" r="6.5" fill="none" stroke="#b0629f" stroke-width="1.5"/><path d="M1.5 8h13M8 1.5c-3 3.5-3 9.5 0 13M8 1.5c3 3.5 3 9.5 0 13" fill="none" stroke="#b0629f" stroke-width="1.2"/></svg>
        www.tranquillybalanced.com
      </li>
      <li>
        <svg viewBox="0 0 16 16"><path d="M8 0.8a5 5 0 0 0-5 5c0 3.8 5 9.4 5 9.4s5-5.6 5-9.4a5 5 0 0 0-5-5zm0 7a2 2 0 1 1 0-4 2 2 0 0 1 0 4z"/></svg>
        <span>250 Aspen Row, Suite 900<br>Boulder, CO, United States, Colorado</span>
      </li>
    </ul>
  </section>
</main>
</body>
</html>
```